RTW Vision and Core Values

We are wanting to promote our core values and vision on posters at our office. I have uploaded a copy of our logo. We would like to incorporate that, the vision and the core values. ALL THREE MUST BE INCLUDED ON THE DESIGN. For reference, our website is www.rtwpetroworks.com

Our vision is:
We are a Team of Power and Strength that Builds our People and Serves our Industry and Communities.

Our Values are:
We Operate with a Standard of Excellence.
We Do the Right Thing Every Time.
We Value and Recognize our People.
We are Team Players.
We Think and Act with Optimism and Faith.

```html
<!DOCTYPE html>
<html lang="en">
<head>
<meta charset="utf-8">
<title>RTW Vision and Core Values Poster</title>
<link href="https://fonts.googleapis.com/css2?family=Poppins:wght@300;400;500;600;700;800&display=swap" rel="stylesheet">
<style>
  :root {
    --navy: #3b4a68;
    --red: #b32a10;
    --blue: #3f6fb0;
    --orange: #d4501d;
    --ink: #262626;
    --band: #1d1d1d;
    --cream: #fbfaf2;
    --backdrop: #6f6f6f;
    --white: #ffffff;
  }
  * { box-sizing: border-box; margin: 0; padding: 0; }
  html, body { width: 1200px; height: 3127px; overflow: hidden; }
  body {
    background: var(--backdrop);
    font-family: "Poppins", sans-serif;
    position: relative;
  }
  .poster {
    position: absolute;
    left: 60px; top: 865px;
    width: 1080px; height: 1397px;
    background: var(--white);
    box-shadow: 0 10px 30px rgba(0,0,0,.35);
    overflow: hidden;
  }
  .title {
    position: absolute; left: 0; top: 62px; width: 100%;
    text-align: center;
    font-weight: 800; font-size: 128px; line-height: 100px;
    letter-spacing: -2px;
  }
  .title .line-navy { color: var(--navy); display: block; }
  .title .line-red { color: var(--red); display: block; }

  .vision-band {
    position: absolute; left: 0; top: 331px; width: 100%; height: 313px;
    background:
      radial-gradient(ellipse at 50% 40%, #3a3a3a 0%, #262626 45%, var(--band) 100%);
  }
  .screw {
    position: absolute; width: 18px; height: 18px; border-radius: 50%;
    background: radial-gradient(circle at 35% 35%, #e4e4e4, #8a8a8a 70%);
    box-shadow: 0 1px 2px rgba(0,0,0,.6);
  }
  .vision-icon { position: absolute; left: 174px; top: 46px; width: 124px; height: 130px; }
  .vision-heading {
    position: absolute; left: 335px; top: 22px;
    color: var(--white); font-size: 78px; line-height: 90px; letter-spacing: -1px;
  }
  .vision-heading .light { font-weight: 300; }
  .vision-heading .bold { font-weight: 700; }
  .vision-text {
    position: absolute; left: 337px; top: 101px; width: 640px;
    color: var(--white); font-weight: 600; font-size: 29px; line-height: 34px;
  }

  .values-tab {
    position: absolute; left: 206px; top: 572px; width: 670px; height: 74px;
  }
  .values-heading {
    position: absolute; left: 0; top: 578px; width: 100%;
    text-align: center; color: var(--red);
    font-size: 68px; line-height: 78px; letter-spacing: -1px; padding-right: 24px;
  }
  .values-heading .light { font-weight: 300; }
  .values-heading .bold { font-weight: 800; }

  .value-card {
    position: absolute; height: 104px;
    background: var(--cream);
    box-shadow: 0 8px 14px -6px rgba(0,0,0,.12);
    display: flex; align-items: center;
    font-weight: 500; font-size: 25px; line-height: 29px; color: var(--ink);
  }
  .value-card.left { left: 86px; width: 350px; justify-content: flex-end; text-align: right; padding-right: 88px; }
  .value-card.right { left: 630px; width: 310px; padding-left: 32px; }

  .hex-chain { position: absolute; left: 0; top: 0; width: 1080px; height: 1397px; }

  .brand-name {
    position: absolute; left: 0; top: 1225px; width: 100%;
    text-align: center; color: var(--navy);
    font-weight: 800; font-size: 84px; line-height: 96px; letter-spacing: 2px;
  }
</style>
</head>
<body>
  <main class="poster">
    <h1 class="title">
      <span class="line-navy">OUR VISION &amp;</span>
      <span class="line-red">CORE VALUES</span>
    </h1>

    <section class="vision-band">
      <span class="screw" style="left:44px;top:29px"></span>
      <span class="screw" style="left:1019px;top:29px"></span>
      <span class="screw" style="left:44px;top:254px"></span>
      <span class="screw" style="left:1019px;top:254px"></span>

      <svg class="vision-icon" viewBox="0 0 124 130" aria-hidden="true">
        <g stroke="#fff" stroke-width="5" stroke-linecap="round">
          <line x1="62" y1="2" x2="62" y2="12"/>
          <line x1="24" y1="18" x2="31" y2="25"/>
          <line x1="100" y1="18" x2="93" y2="25"/>
          <line x1="6" y1="52" x2="16" y2="52"/>
          <line x1="118" y1="52" x2="108" y2="52"/>
          <line x1="20" y1="88" x2="27" y2="81"/>
          <line x1="104" y1="88" x2="97" y2="81"/>
        </g>
        <path d="M62 20a34 34 0 0 0-20 61v10h40V81a34 34 0 0 0-20-61z" fill="#fff"/>
        <rect x="43" y="96" width="38" height="8" rx="3" fill="#fff"/>
        <rect x="47" y="108" width="30" height="8" rx="3" fill="#fff"/>
        <path d="M36 54q26-22 52 0q-26 22-52 0z" fill="#b32a10"/>
        <circle cx="62" cy="54" r="8" fill="#1d1d1d"/>
      </svg>

      <h2 class="vision-heading"><span class="light">OUR </span><span class="bold">VISION IS</span></h2>
      <p class="vision-text">We are a Team of Power and Strength that Builds our People and Serves our Industry and Communities.</p>
    </section>

    <svg class="values-tab" viewBox="0 0 670 74" preserveAspectRatio="none" aria-hidden="true">
      <polygon points="22,0 648,0 670,74 0,74" fill="#fff"/>
    </svg>
    <h2 class="values-heading"><span class="light">OUR </span><span class="bold">VALUES ARE</span></h2>

    <div class="value-card left" style="top:701px">We Operate with a Standard of Excellence.</div>
    <div class="value-card right" style="top:769px">We Do the Right Thing Every Time.</div>
    <div class="value-card left" style="top:851px">We Value and Recognize our People.</div>
    <div class="value-card right" style="top:916px">We are Team Players.</div>
    <div class="value-card left" style="top:987px">We Think and Act with Optimism and Faith.</div>

    <svg class="hex-chain" viewBox="0 0 1080 1397" aria-hidden="true">
      <g fill="none" stroke-width="11" stroke-linejoin="miter">
        <path d="M426 685 L510 685 L549 753 L510 821 L426 821" stroke="var(--red)"/>
        <path d="M640 753 L560 753 L522 821 L560 889 L640 889" stroke="var(--navy)"/>
        <path d="M426 835 L510 835 L549 903 L510 971 L426 971" stroke="var(--blue)"/>
        <path d="M640 900 L560 900 L522 968 L560 1036 L640 1036" stroke="var(--red)"/>
        <path d="M426 971 L510 971 L549 1039 L510 1107 L426 1107" stroke="var(--orange)"/>
      </g>
      <g fill="#3a3a3a">
        <!-- excellence badge -->
        <circle cx="478" cy="748" r="15"/>
        <circle cx="478" cy="748" r="8" fill="#fff"/>
        <path d="M468 760 L463 776 L472 772 L476 780 L478 764 Z M488 760 L493 776 L484 772 L480 780 L478 764 Z"/>
        <!-- right thing gear -->
        <circle cx="590" cy="821" r="18"/>
        <circle cx="590" cy="821" r="11" fill="#fff"/>
        <path d="M583 826 L588 820 L592 823 L598 815" stroke="#3a3a3a" stroke-width="3" fill="none"/>
        <!-- people -->
        <circle cx="470" cy="890" r="6"/><circle cx="486" cy="890" r="6"/>
        <path d="M460 906a10 8 0 0 1 20 0z M476 906a10 8 0 0 1 20 0z"/>
        <path d="M462 918 q10 8 20 4 l14 -8" stroke="#3a3a3a" stroke-width="4" fill="none"/>
        <!-- team -->
        <circle cx="578" cy="964" r="5"/><circle cx="592" cy="964" r="5"/><circle cx="606" cy="964" r="5"/>
        <path d="M570 982a8 9 0 0 1 16 0z M584 982a8 9 0 0 1 16 0z M598 982a8 9 0 0 1 16 0z"/>
        <rect x="574" y="944" width="36" height="5" rx="2"/>
        <!-- optimism -->
        <rect x="472" y="1018" width="12" height="16" rx="2"/>
        <circle cx="464" cy="1046" r="4"/><circle cx="478" cy="1046" r="4"/><circle cx="492" cy="1046" r="4"/>
        <path d="M458 1058a6 6 0 0 1 12 0z M472 1058a6 6 0 0 1 12 0z M486 1058a6 6 0 0 1 12 0z"/>
        <path d="M478 1034 V1040 M464 1040 H492" stroke="#3a3a3a" stroke-width="2"/>
      </g>
    </svg>

    <div class="brand-name">RTW</div>
  </main>
</body>
</html>
```